Business cards for the RT Group

We are looking for a template for our new business cards for our company that we can edit ourselves.
You will find our company colors in the logo. the logo on the back and on the front
first name Last Name
position
E-mail address
mobile number
landline number
Companies we have 2 RT Sicherheit GmbH and RT Services GmbH
address
Lindauer Weg 42
22543 Hamburg
www.rtverbund-beispiel.de

Something modern, simple but professional

if you have any questions, bring it on.

Industry/Entity Type

Sicherheit

Contact Information for Business Card

Steht in der Beschreibung

Colors
F0912C
F2A743
F7CA91
FBE8D2
FDF5EE

Requirements
Must have
• recognition value
Nice to have
• professional
Should not have
• Playful

```html
<!DOCTYPE html>
<html lang="de">
<head>
<meta charset="utf-8">
<title>RT Gruppe – Visitenkarten</title>
<link rel="stylesheet" href="https://fonts.googleapis.com/css2?family=Montserrat:wght@400;500;700;800&display=swap">
<style>
  :root {
    --stage: #d4d4d4;
    --paper: #ffffff;
    --charcoal: #58585a;
    --charcoal-deep: #4e4e50;
    --accent: #f7810f;
    --ink: #3f3f41;
  }
  * { box-sizing: border-box; margin: 0; padding: 0; }
  html, body { width: 1200px; height: 913px; overflow: hidden; }
  body {
    background: var(--stage);
    font-family: "Montserrat", Arial, sans-serif;
    position: relative;
  }
  .card {
    position: absolute;
    width: 540px;
    height: 309px;
    border: 2px solid var(--accent);
    overflow: hidden;
  }
  .card--front { left: 40px; top: 302px; background: var(--paper); }
  .card--back  { left: 620px; top: 302px; background: var(--charcoal); }

  .brand-graphic {
    position: absolute;
    right: 0; top: 0;
    width: 200px; height: 100%;
    background: linear-gradient(180deg, var(--charcoal) 0%, var(--charcoal-deep) 100%);
  }

  .front-content { position: absolute; left: 30px; bottom: 22px; }
  .wordmark {
    font-weight: 800;
    font-size: 30px;
    letter-spacing: 0.5px;
    color: var(--charcoal);
    display: flex; align-items: center; gap: 10px;
    margin-bottom: 14px;
  }
  .wordmark .mark-dot {
    width: 14px; height: 14px; border-radius: 50%; background: var(--accent);
  }
  .person-name {
    font-weight: 700; font-size: 19px; letter-spacing: 1px;
    color: var(--charcoal); text-transform: uppercase;
  }
  .person-role { font-size: 12px; color: var(--ink); margin: 2px 0 10px; }
  .contact-list { list-style: none; }
  .contact-list li {
    display: flex; align-items: center; gap: 10px;
    font-size: 11px; color: var(--ink); line-height: 17px;
  }
  .contact-list svg { width: 11px; height: 11px; fill: var(--accent); flex: none; }

  .back-content {
    position: absolute; inset: 0;
    display: flex; align-items: center; justify-content: center; gap: 16px;
  }
  .wordmark--light { color: #ffffff; font-size: 46px; margin: 0; }
  .wordmark--light .mark-dot { width: 22px; height: 22px; }
</style>
</head>
<body>
  <section class="card card--front" aria-label="Vorderseite der Visitenkarte">
    <div class="brand-graphic" role="img" aria-label="Area for the large brand graphic"></div>
    <div class="front-content">
      <div class="wordmark"><span class="mark-dot"></span>RT Gruppe</div>
      <p class="person-name">Markus Lenz</p>
      <p class="person-role">Managing Director</p>
      <ul class="contact-list">
        <li><svg viewBox="0 0 24 24"><path d="M6.6 10.8a15 15 0 0 0 6.6 6.6l2.2-2.2c.3-.3.7-.4 1-.2 1.1.4 2.3.6 3.6.6.6 0 1 .4 1 1V20c0 .6-.4 1-1 1A17 17 0 0 1 3 4c0-.6.4-1 1-1h3.5c.6 0 1 .4 1 1 0 1.3.2 2.5.6 3.6.1.3 0 .7-.2 1z"/></svg>040-555 010 220</li>
        <li><svg viewBox="0 0 24 24"><path d="M3 7c3-3 15-3 18 0v3h-4V8H7v2H3zM6 11h12l2 9H4zm6 2a3 3 0 1 0 0 6 3 3 0 0 0 0-6z"/></svg>040-555 010 221</li>
        <li><svg viewBox="0 0 24 24"><path d="M2 5h20v14H2zm2 2v.5l8 5 8-5V7z"/></svg>info@rtverbund-beispiel.de</li>
        <li><svg viewBox="0 0 24 24"><path d="M12 2a10 10 0 1 0 0 20 10 10 0 0 0 0-20zm0 2c1 1.5 1.8 3.4 2 6h-4c.2-2.6 1-4.5 2-6zM4.3 14a8 8 0 0 1 0-4h3.8a18 18 0 0 0 0 4zm5.7 0a16 16 0 0 1 0-4h4a16 16 0 0 1 0 4zm5.9 0a18 18 0 0 0 0-4h3.8a8 8 0 0 1 0 4zM12 20c-1-1.5-1.8-3.4-2-6h4c-.2 2.6-1 4.5-2 6z"/></svg>www.rtverbund-beispiel.de</li>
        <li><svg viewBox="0 0 24 24"><path d="M12 2a7 7 0 0 0-7 7c0 5 7 13 7 13s7-8 7-13a7 7 0 0 0-7-7zm0 9.5A2.5 2.5 0 1 1 12 6.5a2.5 2.5 0 0 1 0 5z"/></svg>Lindauer Weg 42</li>
        <li><svg viewBox="0 0 24 24"><path d="M12 2a7 7 0 0 0-7 7c0 5 7 13 7 13s7-8 7-13a7 7 0 0 0-7-7zm0 9.5A2.5 2.5 0 1 1 12 6.5a2.5 2.5 0 0 1 0 5z"/></svg>22543 Hamburg</li>
      </ul>
    </div>
  </section>

  <section class="card card--back" aria-label="Rückseite der Visitenkarte">
    <div class="back-content">
      <div class="wordmark wordmark--light"><span class="mark-dot"></span>RT Gruppe</div>
    </div>
  </section>
</body>
</html>
```